Consulting company with focus on aviation needs

We need a new business card design for our company. The company consults with multiple players in the industry like manufacturers and airlines. It is also a supplier and an inter-company level. Given the targeted industry (aviation) it should be both kind of serious, sound, secure, classy, ​​but also a bit technical, innovative. Should not be too playful, however, "fresh", "airy", "ligth" and "suprising" are suitabe attributes. The existing logo shall be used.

Airlines

```html
<!DOCTYPE html>
<html lang="en">
<head>
<meta charset="utf-8">
<title>Veranto – Business Card</title>
<link rel="stylesheet" href="https://fonts.googleapis.com/css2?family=Open+Sans:wght@400;600&display=swap">
<style>
  :root {
    --stage: #3b3b3b;
    --card: #ffffff;
    --ink-grey: #6d6e70;
    --orange: #f4862f;
    --orange-soft: #f1933a;
    --teal: #2aa58c;
    --text-dark: #333333;
    --white: #ffffff;
  }
  * { margin: 0; padding: 0; box-sizing: border-box; }
  html, body {
    width: 1200px; height: 801px; overflow: hidden;
    background: var(--stage);
    font-family: "Open Sans", Arial, sans-serif;
  }
  .canvas { position: relative; width: 1200px; height: 801px; }
  .card {
    position: absolute; top: 273px; width: 447px; height: 255px;
    background: var(--card); border-radius: 18px; overflow: hidden;
    box-shadow: 0 6px 16px rgba(0,0,0,.45);
  }
  .card--front { left: 135px; }
  .card--back { left: 621px; }

  .brand-mark { position: absolute; border-radius: 50%; background: var(--teal); }
  .brand-name {
    position: absolute; color: var(--ink-grey); font-weight: 400;
    letter-spacing: .18em; white-space: nowrap;
  }
  .tagline { position: absolute; color: var(--orange-soft); white-space: nowrap; }

  .card--front .brand-mark { width: 78px; height: 78px; left: 184px; top: 44px; }
  .card--front .brand-name { left: 0; width: 447px; text-align: center; top: 138px; font-size: 36px; padding-left: .18em; }
  .card--front .tagline { left: 0; width: 447px; text-align: center; top: 184px; font-size: 14px; }

  .card--back .brand-mark { width: 50px; height: 50px; left: 83px; top: 8px; }
  .card--back .brand-name { left: 32px; top: 64px; font-size: 23px; }
  .card--back .tagline { left: 32px; top: 91px; font-size: 9.5px; }

  .name-band {
    position: absolute; left: 0; top: 108px; width: 257px; height: 41px;
    background: var(--orange); color: var(--white);
    padding: 5px 0 0 40px; font-size: 12.5px; line-height: 15px;
  }
  .contact-list { position: absolute; left: 32px; top: 157px; list-style: none; }
  .contact-list li {
    display: flex; align-items: center; height: 20.7px;
    font-size: 11.5px; color: var(--text-dark);
  }
  .contact-list svg { width: 12px; height: 12px; margin-right: 7px; flex: none; }

  .accent-disc {
    position: absolute; left: 262px; top: 52px; width: 190px; height: 190px;
    border-radius: 50%; background: var(--teal);
  }
</style>
</head>
<body>
<main class="canvas">
  <section class="card card--front" aria-label="Card front">
    <span class="brand-mark" aria-hidden="true"></span>
    <p class="brand-name">VERANTO</p>
    <p class="tagline">Linking Partners - Shaping Plans</p>
  </section>

  <section class="card card--back" aria-label="Card back">
    <span class="brand-mark" aria-hidden="true"></span>
    <p class="brand-name">VERANTO</p>
    <p class="tagline">Linking Partners - Shaping Plans</p>

    <div class="name-band">
      <p>Name</p>
      <p>Designation</p>
    </div>

    <ul class="contact-list">
      <li>
        <svg viewBox="0 0 12 12" aria-hidden="true"><circle cx="6" cy="6" r="6" fill="var(--orange)"/><path d="M3.5 4.5 Q6 2.8 8.5 4.5 L8 6 L6.8 5.5 L6.8 4.8 Q6 4.6 5.2 4.8 L5.2 5.5 L4 6 Z" fill="var(--white)"/></svg>
        xxxxxxxxx
      </li>
      <li>
        <svg viewBox="0 0 12 12" aria-hidden="true"><circle cx="6" cy="6" r="6" fill="var(--orange)"/><path d="M6 2.5 A2.2 2.2 0 0 1 8.2 4.7 C8.2 6.3 6 9.3 6 9.3 C6 9.3 3.8 6.3 3.8 4.7 A2.2 2.2 0 0 1 6 2.5 Z" fill="var(--white)"/><circle cx="6" cy="4.7" r=".9" fill="var(--orange)"/></svg>
        xxxxxxxxx
      </li>
      <li>
        <svg viewBox="0 0 12 12" aria-hidden="true"><circle cx="6" cy="6" r="6" fill="var(--orange)"/><rect x="3" y="4" width="6" height="4.2" fill="none" stroke="var(--white)" stroke-width=".9"/><path d="M3 4 L6 6.4 L9 4" fill="none" stroke="var(--white)" stroke-width=".9"/></svg>
        xxxxx@veranto.com
      </li>
      <li>
        <svg viewBox="0 0 12 12" aria-hidden="true"><circle cx="6" cy="6" r="6" fill="var(--orange)"/><circle cx="6" cy="6" r="3.3" fill="none" stroke="var(--white)" stroke-width=".8"/><ellipse cx="6" cy="6" rx="1.4" ry="3.3" fill="none" stroke="var(--white)" stroke-width=".8"/><path d="M2.7 6 H9.3" stroke="var(--white)" stroke-width=".8"/></svg>
        www.veranto.com
      </li>
    </ul>

    <span class="accent-disc" aria-hidden="true"></span>
  </section>
</main>
</body>
</html>
```